Stationery Design Project

Hi All,

We need you to design stationary for a new Business and Accounting Advisory Firm. We have already got the logo designed and it is attached. If you could also if possible, match the fonts in your design to that on the logo’s provided.

What we need:
- Business Card
- A4 Letter head
- A4 Folders
- PPT template (Title page and regular page)

And what ever else you want to throw in.

We are in the process of getting the web site designed, however below is a list of websites which we like which will give you an understanding of the style that we are going for.

- plavoni.com
- brightfunnelo.com
- hourquillet.com
- artmarrowly.com

I look forward to your seeing your design.

Hi All,

I have just realised that I forgot that i need to include a Licensed Tallymasters image on the letter head, please find attaced as File 1. Could you please have this image in the bottom left header.

Regards,

Gareth

Industry/Entity Type

Business

Requirements
Must have
• Outputs:
- Documents ready to print
- Generic editable information
- Pdf copies of the documents
- Word version of letterhead

```html
<!DOCTYPE html>
<html lang="en">
<head>
<meta charset="utf-8">
<title>Tarrowby Partners — Stationery</title>
<link rel="stylesheet" href="https://fonts.googleapis.com/css2?family=EB+Garamond:wght@500&family=Arimo:wght@400;700&display=swap">
<style>
  :root {
    --orange: #f47b20;
    --yellow: #f9c332;
    --navy: #3a5a9a;
    --cyan: #3ab5d2;
    --ink: #2e4a8f;
    --paper: #ffffff;
    --stage: #eceff2;
    --edge: #c9ced4;
    --serif: "EB Garamond", Georgia, serif;
    --sans: "Arimo", Arial, sans-serif;
  }
  * { box-sizing: border-box; margin: 0; padding: 0; }
  html, body { width: 1200px; height: 900px; overflow: hidden; }
  body { background: var(--stage); font-family: var(--sans); position: relative; }

  .sheet { position: absolute; background: var(--paper); border: 1px solid var(--edge); overflow: hidden; }

  /* brand lockup */
  .brand { display: flex; align-items: center; gap: 8px; }
  .brand-dot { border-radius: 50%; background: var(--orange); flex: none; }
  .brand-name { font-family: var(--serif); font-weight: 500; color: var(--ink); white-space: nowrap; }

  .web { font-family: var(--sans); letter-spacing: 0.18em; white-space: nowrap; }
  .contact { font-family: var(--sans); color: #fff; line-height: 1.45; white-space: nowrap; }

  /* A4 folder front */
  .folder { left: 60px; top: 120px; width: 300px; height: 424px; }
  .folder .top-band { position: absolute; left: 0; top: 0; width: 100%; height: 22px; background: var(--orange); border-bottom: 3px solid var(--yellow); }
  .folder .brand { position: absolute; left: 28px; top: 52px; }
  .folder .brand-dot { width: 26px; height: 26px; }
  .folder .brand-name { font-size: 22px; }
  .folder .foot { position: absolute; left: 0; bottom: 0; width: 100%; height: 78px; background: var(--navy); border-top: 4px solid var(--cyan); }
  .folder .web { position: absolute; right: 18px; bottom: 90px; font-size: 8px; color: var(--cyan); }
  .folder .contact { position: absolute; left: 20px; top: 16px; font-size: 8px; }

  /* A4 letterhead */
  .letter { left: 400px; top: 120px; width: 300px; height: 424px; }
  .letter .brand { position: absolute; left: 28px; top: 34px; }
  .letter .brand-dot { width: 20px; height: 20px; }
  .letter .brand-name { font-size: 18px; }
  .letter .foot { position: absolute; left: 0; bottom: 0; width: 100%; height: 70px; background: var(--orange); border-top: 3px solid var(--yellow); }
  .letter .contact { position: absolute; left: 18px; top: 12px; font-size: 7.5px; }
  .letter .web { position: absolute; left: 18px; bottom: 80px; font-size: 7.5px; color: var(--orange); }
  .letter .badge { position: absolute; right: 14px; top: 14px; width: 74px; height: 42px; background: #fff; border-radius: 6px; }

  /* business cards */
  .card-front { left: 798px; top: 77px; width: 163px; height: 113px; }
  .card-front .brand { position: absolute; left: 12px; top: 26px; gap: 5px; }
  .card-front .brand-dot { width: 14px; height: 14px; }
  .card-front .brand-name { font-size: 14px; }
  .card-front .foot { position: absolute; left: 0; bottom: 0; width: 100%; height: 41px; background: var(--orange); border-top: 2px solid var(--yellow); }
  .card-front .web { position: absolute; right: 14px; top: 15px; font-size: 5.5px; color: #fff; }

  .card-back { left: 989px; top: 77px; width: 175px; height: 113px; }
  .card-back .person { position: absolute; left: 14px; top: 19px; }
  .card-back .person-name { font-family: var(--serif); font-weight: 500; font-size: 8.5px; color: var(--ink); }
  .card-back .person-role { font-size: 5.5px; color: var(--cyan); margin-top: 3px; }
  .card-back .web { position: absolute; right: 14px; top: 62px; font-size: 5.5px; color: var(--cyan); letter-spacing: 0.08em; }
  .card-back .foot { position: absolute; left: 0; bottom: 0; width: 100%; height: 37px; background: var(--navy); border-top: 2px solid var(--cyan); }
  .card-back .contact { position: absolute; left: 14px; top: 5px; font-size: 5.2px; }

  /* presentation slides */
  .slide { left: 787px; width: 377px; height: 284px; }
  .slide-title { top: 264px; }
  .slide-title .brand { position: absolute; left: 50%; top: 38px; transform: translateX(-50%); gap: 9px; }
  .slide-title .brand-dot { width: 30px; height: 30px; }
  .slide-title .brand-name { font-size: 24px; }
  .slide-title .deck-name { position: absolute; left: 0; width: 100%; top: 128px; text-align: center; font-family: var(--serif); font-weight: 500; font-size: 23px; letter-spacing: 0.08em; color: var(--ink); }
  .slide-title .foot { position: absolute; left: 0; bottom: 0; width: 100%; height: 75px; background: var(--orange); border-top: 4px solid var(--yellow); }
  .slide-title .web { position: absolute; left: 0; width: 100%; top: 30px; text-align: center; font-size: 7.5px; color: #fff; letter-spacing: 0.3em; }

  .slide-page { top: 570px; }
  .slide-page .deck-name { position: absolute; right: 30px; bottom: 40px; font-size: 8px; letter-spacing: 0.12em; color: var(--cyan); }
  .slide-page .foot { position: absolute; left: 0; bottom: 0; width: 100%; height: 35px; background: var(--navy); border-top: 4px solid var(--cyan); }
</style>
</head>
<body>

<section class="sheet folder" aria-label="A4 folder front">
  <div class="top-band"></div>
  <div class="brand"><span class="brand-dot"></span><span class="brand-name">Tarrowby Partners</span></div>
  <div class="web">www.tarrowbypartners.com</div>
  <div class="foot">
    <p class="contact">A: 12 Keel Street, Norbury, Westvale<br>T: 555-010-2040 &middot; F: 555-010-2041<br>E: hello@tarrowby.com</p>
  </div>
</section>

<section class="sheet letter" aria-label="A4 letterhead">
  <div class="brand"><span class="brand-dot"></span><span class="brand-name">Tarrowby Partners</span></div>
  <div class="web">www.tarrowbypartners.com</div>
  <div class="foot">
    <p class="contact">A: 12 Keel Street, Norbury, Westvale<br>T: 555-010-2040 &middot; F: 555-010-2041<br>E: hello@tarrowby.com</p>
    <div class="badge" role="img" aria-label="Licensed Tallymasters membership badge"></div>
  </div>
</section>

<section class="sheet card-front" aria-label="Business card front">
  <div class="brand"><span class="brand-dot"></span><span class="brand-name">Tarrowby Partners</span></div>
  <div class="foot"><div class="web">www.tarrowbypartners.com</div></div>
</section>

<section class="sheet card-back" aria-label="Business card back">
  <div class="person">
    <p class="person-name">Firstname Lastname</p>
    <p class="person-role">Position position</p>
  </div>
  <div class="web">www.tarrowbypartners.com</div>
  <div class="foot">
    <p class="contact">A: 12 Keel Street, Norbury, Westvale<br>T: 555-010-2040 &middot; F: 555-010-2041 &middot; M: 555-010-2042<br>E: hello@tarrowby.com</p>
  </div>
</section>

<section class="sheet slide slide-title" aria-label="Presentation title slide">
  <div class="brand"><span class="brand-dot"></span><span class="brand-name">Tarrowby Partners</span></div>
  <h1 class="deck-name">Presentation name</h1>
  <div class="foot"><div class="web">www.tarrowbypartners.com</div></div>
</section>

<section class="sheet slide slide-page" aria-label="Presentation content slide">
  <p class="deck-name">Presentation name</p>
  <div class="foot"></div>
</section>

</body>
</html>
```